Stationery For Upscale Concierge Company

Create stationary that looks good in black and white and uses the attached logo. Needs to be upscale using upscale fonts and layout. Use the attached logo. Reverse out if necessary.

```html
<!DOCTYPE html>
<html lang="en">
<head>
<meta charset="UTF-8">
<title>Meridian Concierge – Business Cards</title>
<link rel="stylesheet" href="https://fonts.googleapis.com/css2?family=Oswald:wght@500&family=Open+Sans:ital,wght@0,400;1,400&display=swap">
<style>
  :root {
    --backdrop: #4f4640;
    --card-black: #0a0b0b;
    --ink-white: #ffffff;
    --gold-light: #f2cf4a;
    --gold-mid: #d9a929;
    --gold-deep: #a9781a;
    --text-soft: #e9e9e9;
  }
  * { margin: 0; padding: 0; box-sizing: border-box; }
  html, body { width: 1200px; height: 1200px; overflow: hidden; }
  body {
    background: var(--backdrop);
    position: relative;
    font-family: "Open Sans", sans-serif;
  }
  .card {
    position: absolute;
    width: 560px;
    height: 320px;
    background: var(--card-black);
    box-shadow: 0 14px 30px rgba(0,0,0,0.45);
  }
  .card--front { left: 80px; top: 170px; }
  .card--back { left: 560px; top: 690px; }

  /* Front: company name */
  .brand {
    position: absolute;
    inset: 0;
    display: flex;
    align-items: center;
    justify-content: center;
    gap: 18px;
  }
  .brand__dot {
    width: 22px; height: 22px;
    border-radius: 50%;
    background: var(--ink-white);
  }
  .brand__name {
    font-family: "Open Sans", sans-serif;
    font-weight: 400;
    font-size: 34px;
    letter-spacing: 5px;
    text-transform: uppercase;
    color: var(--ink-white);
  }

  /* Back: contact */
  .identity {
    position: absolute;
    right: 322px;
    top: 122px;
    text-align: right;
  }
  .identity__name {
    font-family: "Oswald", sans-serif;
    font-weight: 500;
    font-size: 25px;
    line-height: 1.1;
    letter-spacing: 0.3px;
    text-transform: uppercase;
    background: linear-gradient(180deg, var(--gold-light), var(--gold-mid) 55%, var(--gold-deep));
    -webkit-background-clip: text;
    background-clip: text;
    color: transparent;
  }
  .identity__title {
    font-style: italic;
    font-size: 15px;
    color: var(--text-soft);
    margin-top: 2px;
  }
  .divider {
    position: absolute;
    left: 252px;
    top: 124px;
    width: 1.5px;
    height: 60px;
    background: var(--gold-mid);
  }
  .contact {
    position: absolute;
    left: 268px;
    top: 124px;
    list-style: none;
  }
  .contact__item {
    display: flex;
    align-items: center;
    gap: 9px;
    font-size: 15.5px;
    line-height: 20px;
    color: var(--text-soft);
  }
  .contact__icon { width: 12px; height: 12px; fill: var(--gold-mid); flex: none; }

  .gold-rule {
    position: absolute;
    left: 0;
    right: 0;
    background: linear-gradient(90deg, var(--gold-deep), var(--gold-light) 40%, var(--gold-mid) 70%, var(--gold-deep));
  }
  .gold-rule--thin { bottom: 26px; height: 3px; }
  .gold-rule--thick { bottom: 8px; height: 6px; }
</style>
</head>
<body>

  <section class="card card--front" aria-label="Business card front">
    <div class="brand">
      <span class="brand__dot"></span>
      <span class="brand__name">Meridian Concierge</span>
    </div>
  </section>

  <section class="card card--back" aria-label="Business card back">
    <div class="identity">
      <p class="identity__name">Adrian Cole</p>
      <p class="identity__title">President</p>
    </div>
    <span class="divider"></span>
    <ul class="contact">
      <li class="contact__item">
        <svg class="contact__icon" viewBox="0 0 24 24" aria-hidden="true"><path d="M6.6 10.8a15.1 15.1 0 0 0 6.6 6.6l2.2-2.2a1 1 0 0 1 1-.25 11.4 11.4 0 0 0 3.6.57 1 1 0 0 1 1 1V20a1 1 0 0 1-1 1A17 17 0 0 1 3 4a1 1 0 0 1 1-1h3.5a1 1 0 0 1 1 1c0 1.25.2 2.45.57 3.57a1 1 0 0 1-.25 1z"/></svg>
        (555) 014-2290
      </li>
      <li class="contact__item">
        <svg class="contact__icon" viewBox="0 0 24 24" aria-hidden="true"><path d="M2 5h20v14H2z M2 5l10 8 10-8" fill="none" stroke="#d9a929" stroke-width="2.5"/></svg>
        info@meridianhost.com
      </li>
      <li class="contact__item">
        <svg class="contact__icon" viewBox="0 0 24 24" aria-hidden="true"><circle cx="12" cy="12" r="10" fill="none" stroke="#d9a929" stroke-width="2.5"/><path d="M2 12h20M12 2c3 3 3 17 0 20M12 2c-3 3-3 17 0 20" fill="none" stroke="#d9a929" stroke-width="2"/></svg>
        www.meridianhost.com
      </li>
    </ul>
    <span class="gold-rule gold-rule--thin"></span>
    <span class="gold-rule gold-rule--thick"></span>
  </section>

</body>
</html>
```